WordPress Website Design Project

Technical & Functional Deliverables
WordPress CMS
Fully responsive design
Integrated WhatsApp chatbot
Custom article filtering system
SEO-friendly site structure & performance optimization
CMS user manual & training session
Updates

Need extra days to review

Industry/Entity Type

Industrial Safety and Compliance

Coding

Coded - Design and coding required

Number of Pages Required

5+ page

Font styles to use
Sans Serif

Colors
0054AA
0677BA
7BADD7
CADEEF
E8F1F8

```html
<!DOCTYPE html>
<html lang="en">
<head>
<meta charset="utf-8">
<title>Halvard — Industrial Safety &amp; Compliance</title>
<link href="https://fonts.googleapis.com/css2?family=Poppins:wght@400;500;600;700&display=swap" rel="stylesheet">
<style>
:root{
  --navy:#1c2d50;
  --navy-deep:#16243f;
  --blue:#0054aa;
  --mid:#0677ba;
  --sky:#7badd7;
  --pale:#cadeef;
  --mist:#e8f1f8;
  --accent:#5a8fd0;
  --ink:#1a1a1a;
  --white:#fff;
}
*{box-sizing:border-box;margin:0;padding:0}
html,body{width:1200px;height:3017px;overflow:hidden}
body{position:relative;font-family:'Poppins',sans-serif;color:var(--ink);background:var(--white)}
.abs{position:absolute}

/* header */
.site-header{position:absolute;left:0;top:0;width:1200px;height:116px;background:var(--white)}
.brand{position:absolute;display:flex;align-items:center;gap:12px;font-weight:700;letter-spacing:2px}
.brand-mark{background:var(--accent)}
.brand--header{left:69px;top:26px;font-size:54px;color:var(--navy)}
.brand--header .brand-mark{width:64px;height:66px}
.nav{position:absolute;top:52px;left:492px;display:flex;align-items:center;font-size:14px;color:var(--navy)}
.nav a{color:inherit;text-decoration:none}
.nav .active{background:var(--accent);color:var(--white);padding:1px 12px}
.nav .sep{margin:0 36px;font-weight:600}
.btn-header{position:absolute;left:1011px;top:36px;width:122px;height:46px;background:var(--navy);color:var(--white);font-size:14px;font-weight:500;display:flex;align-items:center;justify-content:center}

/* hero */
.hero{position:absolute;left:0;top:116px;width:1200px;height:699px;background:linear-gradient(180deg,#22375d,#1b2c4c 60%,#2a3c5c)}
.hero-side{position:absolute;left:858px;top:0;width:342px;height:699px;background:linear-gradient(180deg,#7aa6d8,#5c8ccc)}
.hero-kicker{position:absolute;left:67px;top:128px;font-size:37px;font-weight:600;color:var(--accent)}
.hero-title{position:absolute;left:66px;top:178px;font-size:81px;line-height:86px;font-weight:700;color:var(--white)}
.hero-title .hl{color:var(--accent)}
.btn-outline{position:absolute;left:69px;top:477px;width:303px;height:79px;border:2px solid var(--white);color:var(--white);font-size:26px;font-weight:600;display:flex;align-items:center;padding-left:42px;gap:38px}
.btn-outline .sq{width:32px;height:32px;background:var(--accent)}
.hero-block{position:absolute;left:995px;top:398px;width:173px;height:198px;background:var(--white)}
.hero-frame{position:absolute;left:613px;top:121px;width:531px;height:453px;border:2px solid var(--white)}
.hero-photo{position:absolute;left:622px;top:128px;width:513px;height:439px;background:linear-gradient(135deg,#d6dde6,#9aa6b4 45%,#3a3f48)}

/* articles */
.section-mark{position:absolute;left:522px;top:931px;display:flex;align-items:center;gap:10px}
.section-mark .line{width:55px;height:3px;background:var(--accent)}
.section-mark .sq{width:28px;height:28px;background:var(--accent)}
.section-title{position:absolute;left:0;top:955px;width:1200px;text-align:center;font-size:66px;font-weight:700;color:var(--navy)}
.search{position:absolute;left:66px;top:1084px;width:386px;height:63px;border:1px solid #8a8f99;border-radius:32px;padding-left:28px;display:flex;align-items:center;font-size:15px;color:#888}
.search svg{position:absolute;right:28px;top:16px}
.btn-filter{position:absolute;left:1015px;top:1098px;width:119px;height:35px;border-radius:18px;background:var(--navy);color:var(--white);font-size:14px;display:flex;align-items:center;justify-content:center}
.rule{position:absolute;left:69px;top:1193px;width:1065px;height:2px;background:#5f7ea8}
.locations{position:absolute;top:1226px;left:66px;font-size:16px;color:var(--ink)}
.loc{position:absolute;top:1226px;font-size:16px;display:flex;align-items:center;gap:8px}
.loc i{display:block;width:15px;height:15px;border:2px solid var(--navy);border-radius:50%}
.btn-view{position:absolute;left:895px;top:1223px;width:100px;height:29px;border-radius:15px;background:var(--accent);color:var(--white);font-size:12px;display:flex;align-items:center;justify-content:center;gap:14px}
.card{position:absolute;width:248px}
.card-img{height:215px;border-radius:6px;position:relative}
.tag{position:absolute;left:21px;top:26px;width:78px;height:30px;background:var(--white);font-size:12px;font-weight:500;display:flex;align-items:center;justify-content:center}
.card-date{margin:22px 0 0 21px;font-size:13px;color:var(--accent);display:flex;align-items:center;gap:6px}
.card-title{margin:6px 0 0 21px;font-size:16.5px;line-height:24px;font-weight:600;color:var(--ink);width:215px}
.btn-load{position:absolute;left:449px;top:2515px;width:303px;height:80px;background:var(--navy);color:var(--white);font-size:26px;font-weight:600;display:flex;align-items:center;padding-left:52px;gap:48px}
.btn-load .sq{width:32px;height:32px;background:var(--accent)}

/* footer */
.site-footer{position:absolute;left:0;top:2697px;width:1200px;height:320px;background:var(--navy)}
.footer-about{position:absolute;left:217px;top:60px;font-size:17px;line-height:27px;color:var(--white);text-align:center}
.footer-links{position:absolute;left:802px;top:57px;list-style:none;font-size:15px;line-height:26px;color:var(--white)}
.footer-links li{display:flex;align-items:center;gap:10px}
.footer-links li::before{content:"";width:10px;height:10px;background:var(--accent)}
.footer-rule{position:absolute;left:69px;top:202px;width:1065px;height:1px;background:#7d8aa4}
.legal{position:absolute;left:69px;top:241px;font-size:14px;color:var(--white)}
.social{position:absolute;left:69px;top:280px;width:22px;height:22px;border-radius:50%;background:var(--accent)}
.copy{position:absolute;left:0;top:254px;width:1148px;text-align:center;font-size:14px;color:var(--white)}
.brand--footer{left:842px;top:228px;font-size:56px;color:var(--white)}
.brand--footer .brand-mark{width:64px;height:68px}
</style>
</head>
<body>
<header class="site-header">
  <div class="brand brand--header"><span class="brand-mark"></span>HALVARD</div>
  <nav class="nav">
    <a class="active" href="#">HOME</a><span class="sep">|</span>
    <a href="#">ABOUT US</a><span class="sep">|</span>
    <a href="#">SOLUTIONS</a><span class="sep">|</span>
    <a href="#">ARTICLES</a>
  </nav>
  <a class="btn-header">CONTACT US</a>
</header>

<section class="hero">
  <div class="hero-side"></div>
  <p class="hero-kicker">Your Partner In</p>
  <h1 class="hero-title">INDUSTRIAL<br>SAFETY &amp;<br><span class="hl">Compliance</span></h1>
  <a class="btn-outline">CONTACT US<span class="sq"></span></a>
  <div class="hero-block"></div>
  <div class="hero-frame"></div>
  <div class="hero-photo" role="img" aria-label="Colleagues working together at laptops in a bright office"></div>
</section>

<div class="section-mark"><span class="line"></span><span class="sq"></span><span class="line"></span></div>
<h2 class="section-title">ARTICLES</h2>
<div class="search">Search News
  <svg width="32" height="32" viewBox="0 0 32 32" fill="none" stroke="#555" stroke-width="2"><circle cx="13" cy="13" r="10"/><line x1="20" y1="20" x2="29" y2="29"/></svg>
</div>
<a class="btn-filter">Filter News</a>
<div class="rule"></div>
<span class="locations">Locations</span>
<span class="loc" style="left:237px"><i></i>Americas</span>
<span class="loc" style="left:404px"><i></i>Asia Pacific</span>
<span class="loc" style="left:589px"><i></i>Europe</span>
<span class="loc" style="left:755px"><i></i>Uk, India</span>
<a class="btn-view">View All <span>+</span></a>

<div class="cards">
  <article class="card" style="left:69px;top:1340px"><div class="card-img" role="img" aria-label="Aerial view of a town with green fields" style="background:linear-gradient(160deg,#7ea7d4,#8a9a6a 50%,#5c7a48)"><span class="tag">News</span></div><p class="card-date">▦ Apr 25, 2022</p><h3 class="card-title">Lorem ipsum dolor sit elit, slit tetur elit dol dolor dolor sit elit</h3></article>
  <article class="card" style="left:341px;top:1340px"><div class="card-img" role="img" aria-label="Aerial view of a road beside a waterway" style="background:linear-gradient(160deg,#6a8a6a,#9aa4ac 50%,#c3c9cf)"><span class="tag">News</span></div><p class="card-date">▦ Apr 25, 2022</p><h3 class="card-title">Lorem ipsum dolor sit elit, slit tetur elit dol dolor dolor sit elit</h3></article>
  <article class="card" style="left:614px;top:1340px"><div class="card-img" role="img" aria-label="Passenger ferry at a harbour pier" style="background:linear-gradient(180deg,#7fb0e0,#c9c5bd 40%,#3aa7b8)"><span class="tag">News</span></div><p class="card-date">▦ Apr 25, 2022</p><h3 class="card-title">Lorem ipsum dolor sit elit, slit tetur elit dol dolor dolor sit elit</h3></article>
  <article class="card" style="left:886px;top:1340px"><div class="card-img" role="img" aria-label="Modern concrete and timber building" style="background:linear-gradient(135deg,#c9d9e8,#8a8a82 50%,#5a5446)"><span class="tag">News</span></div><p class="card-date">▦ Apr 25, 2022</p><h3 class="card-title">Lorem ipsum dolor sit elit, slit tetur elit dol dolor dolor sit elit</h3></article>

  <article class="card" style="left:69px;top:1719px"><div class="card-img" role="img" aria-label="Glass office towers at sunset" style="background:linear-gradient(120deg,#3e5a78,#7b9ab8 50%,#e8c878)"><span class="tag">News</span></div><p class="card-date">▦ Apr 25, 2022</p><h3 class="card-title">Lorem ipsum dolor sit elit, slit tetur elit dol dolor dolor sit elit</h3></article>
  <article class="card" style="left:341px;top:1719px"><div class="card-img" role="img" aria-label="Portrait of business people" style="background:linear-gradient(120deg,#b83a34,#d8c8b8 45%,#2a2e3a)"><span class="tag">News</span></div><p class="card-date">▦ Apr 25, 2022</p><h3 class="card-title">Lorem ipsum dolor sit elit, slit tetur elit dol dolor dolor sit elit</h3></article>
  <article class="card" style="left:614px;top:1719px"><div class="card-img" role="img" aria-label="Historic stone college building" style="background:linear-gradient(160deg,#4a78c8,#b8a478 50%,#7a6a52)"><span class="tag">News</span></div><p class="card-date">▦ Apr 25, 2022</p><h3 class="card-title">Lorem ipsum dolor sit elit, slit tetur elit dol dolor dolor sit elit</h3></article>
  <article class="card" style="left:886px;top:1719px"><div class="card-img" role="img" aria-label="Colleagues in an office meeting" style="background:linear-gradient(135deg,#d6dde6,#9aa6b4 45%,#3a3f48)"><span class="tag">News</span></div><p class="card-date">▦ Apr 25, 2022</p><h3 class="card-title">Lorem ipsum dolor sit elit, slit tetur elit dol dolor dolor sit elit</h3></article>

  <article class="card" style="left:69px;top:2106px"><div class="card-img" role="img" aria-label="Dense city skyline at dusk" style="background:linear-gradient(180deg,#c8a898,#8a7a78 50%,#4a4a52)"><span class="tag">News</span></div><p class="card-date">▦ Apr 25, 2022</p><h3 class="card-title">Lorem ipsum dolor sit elit, slit tetur elit dol dolor dolor sit elit</h3></article>
  <article class="card" style="left:341px;top:2106px"><div class="card-img" role="img" aria-label="Aerial view of a green river park" style="background:linear-gradient(160deg,#8a8a6a,#5a7a3a 50%,#6a9aa8)"><span class="tag">News</span></div><p class="card-date">▦ Apr 25, 2022</p><h3 class="card-title">Lorem ipsum dolor sit elit, slit tetur elit dol dolor dolor sit elit</h3></article>
  <article class="card" style="left:614px;top:2106px"><div class="card-img" role="img" aria-label="Residential towers covered in greenery" style="background:linear-gradient(180deg,#a8c8e8,#6a8a58 50%,#4a5a48)"><span class="tag">News</span></div><p class="card-date">▦ Apr 25, 2022</p><h3 class="card-title">Lorem ipsum dolor sit elit, slit tetur elit dol dolor dolor sit elit</h3></article>
  <article class="card" style="left:886px;top:2106px"><div class="card-img" role="img" aria-label="Civic building beside a river" style="background:linear-gradient(180deg,#b8c8d8,#c8b898 55%,#7a6a5a)"><span class="tag">News</span></div><p class="card-date">▦ Apr 25, 2022</p><h3 class="card-title">Lorem ipsum dolor sit elit, slit tetur elit dol dolor dolor sit elit</h3></article>
</div>

<a class="btn-load">LOAD MORE<span class="sq"></span></a>

<footer class="site-footer">
  <p class="footer-about">We are Halvard. Your<br>Partner in Industrial<br>Safety and Compliance</p>
  <ul class="footer-links"><li>About Us</li><li>Solutions</li><li>Articles</li><li>Contact Us</li></ul>
  <div class="footer-rule"></div>
  <p class="legal">Legal | Cookies | Privacy</p>
  <span class="social" aria-label="Social link"></span>
  <p class="copy">(C) Halvard (S) Pte Ltd 2025</p>
  <div class="brand brand--footer"><span class="brand-mark"></span>HALVARD</div>
</footer>
</body>
</html>
```